Speisekarten-Design für Bistro und Café
Zielgruppe
Bistro und Café in der Eifel mit gemischten Publikum . Aber eher jünger modernere Gäste . Wir sind auch ein junges Team .
Bieten Frühstück, kaffee und Kuchen, Waffeln Burger, und Cocktails , Wein und co an
Aufgabenstellung
Gerne etwas modernes und Frisches in DIN a 4 im Anhang wie es aussehen könnte in die Richtung wäre es super . Gerne bunt und modern .

```html
<!DOCTYPE html>
<html lang="de">
<head>
<meta charset="utf-8">
<title>Bistro and Cafe – Speisekarte</title>
<link rel="stylesheet" href="https://fonts.googleapis.com/css2?family=Archivo+Black&family=Montserrat:ital,wght@0,400;0,600;0,700;1,700&display=swap">
<style>
:root{
  --backdrop:#cec4b8;
  --paper:#f8f7f5;
  --ink:#1d1c1b;
  --muted:#6d6862;
  --sand:#d7c7b1;
  --sand-deep:#c4ac8a;
  --espresso:#2a2622;
}
*{box-sizing:border-box;margin:0;padding:0}
html,body{width:1200px;height:3181px;overflow:hidden}
body{background:var(--backdrop);font-family:"Montserrat",sans-serif;color:var(--ink);position:relative}
.stage{position:absolute;left:0;width:1200px;height:795px}
.page{position:absolute;width:500px;height:707px;background:var(--paper);overflow:hidden;box-shadow:0 10px 28px rgba(60,45,30,.18)}
.spread .page-left{left:100px;top:44px}
.spread .page-right{left:600px;top:44px}
.spread .page-left::after{content:"";position:absolute;right:0;top:0;width:30px;height:100%;background:linear-gradient(90deg,transparent,rgba(0,0,0,.08))}
.photo{position:absolute}
.display{font-family:"Archivo Black",sans-serif;text-transform:uppercase;line-height:.92;letter-spacing:.5px}
.vertical{position:absolute;writing-mode:vertical-rl;transform:rotate(180deg);white-space:nowrap}
.amp{font-family:"Montserrat",sans-serif;font-style:italic;font-weight:700;text-transform:lowercase;color:var(--sand-deep);font-size:.42em;letter-spacing:0;padding:6px 0}

/* cover */
.cover{left:374px;top:78px;width:452px;height:640px}
.cover-photo{left:0;top:0;width:290px;height:640px;background:radial-gradient(circle at 45% 35%,#6e4a30 0,#3d2b1f 35%,#26221f 70%)}
.cover-title{right:30px;bottom:24px;font-size:64px;color:var(--ink)}

/* section blocks */
.block{position:absolute}
.label{font-size:9px;color:var(--muted);margin-bottom:3px}
.headline{font-size:22px;margin-bottom:14px}
.item{margin-bottom:11px;width:100%}
.item-row{display:flex;align-items:baseline;font-size:8px;font-weight:700}
.leader{flex:1;border-bottom:1px dotted var(--muted);margin:0 4px;transform:translateY(-2px)}
.price{font-weight:400}
.desc{font-size:7px;color:var(--muted);margin-top:2px;line-height:1.3}
.drink{display:flex;align-items:baseline;font-size:7.2px;margin-bottom:3px}
.vol{width:26px;color:var(--muted)}
.divider{position:absolute;width:1px;background:#b9b2aa}
.mood{position:absolute;font-family:"Archivo Black",sans-serif;color:var(--sand-deep);text-transform:uppercase;text-align:center;font-size:17px;line-height:1}
.rule{position:absolute;height:2px;background:var(--sand-deep)}
.circle-mark{position:absolute;border:1px solid var(--sand);border-radius:50%}
.sand-panel{position:absolute;background:var(--sand)}
</style>
</head>
<body>

<!-- Cover -->
<section class="stage" style="top:0">
  <div class="page cover">
    <div class="photo cover-photo" role="img" aria-label="Drei Cappuccinotassen mit Latte Art von oben auf dunklem Holztisch"></div>
    <h1 class="display vertical cover-title">Bistro<span class="amp">and</span>Cafe</h1>
  </div>
</section>

<!-- Spread 1: Kaffee & Kuchen -->
<section class="stage spread" style="top:795px">
  <div class="page page-left">
    <div class="photo" style="inset:0;background:linear-gradient(180deg,#5b4332 0,#7a5a41 35%,#c9bfb4 60%,#e6e1da 100%)" role="img" aria-label="Waffeln mit Sirup auf einem Teller, Kaffeebohnen daneben"></div>
    <h2 class="display vertical" style="left:24px;bottom:60px;font-size:52px;color:#fff">Coffee<span class="amp" style="color:#fff">and</span>Cake</h2>
  </div>
  <div class="page page-right">
    <div class="block" style="left:60px;top:70px;width:210px">
      <p class="label">Cake &amp; Waffles</p>
      <h3 class="display headline">Sweet<br>Party</h3>
      <div class="item"><div class="item-row">The BIG BRO<span class="leader"></span><span class="price">€ 2,30</span></div><p class="desc">Belgische Waffel, Kirschen und Sahne</p></div>
      <div class="item"><div class="item-row">The BIG BRO<span class="leader"></span><span class="price">€ 2,30</span></div><p class="desc">Hausgemachter Käsekuchen mit Beeren dazu</p></div>
      <div class="item"><div class="item-row">The BIG BRO<span class="leader"></span><span class="price">€ 2,30</span></div><p class="desc">Schokoladentorte mit Vanilleeis und Minze</p></div>
    </div>

    <div class="sand-panel" style="left:300px;top:150px;width:170px;height:510px"></div>
    <div class="photo" style="left:285px;top:60px;width:175px;height:150px;background:linear-gradient(135deg,#8a7563,#d9b98a 45%,#5a4a3e)" role="img" aria-label="Frühstückstisch mit Kaffee, Orangensaft und Croissants"></div>

    <div class="block" style="left:305px;top:245px;width:150px">
      <p class="label">Frühstück</p>
      <h3 class="display headline">Good<br>Morning</h3>
      <div class="item"><div class="item-row">The BIG BRO<span class="leader"></span><span class="price">€ 2,30</span></div><p class="desc">Zwei Brötchen, Butter und Marmelade</p></div>
      <div class="item"><div class="item-row">The BIG BRO<span class="leader"></span><span class="price">€ 2,30</span></div><p class="desc">Rührei mit Speck und Toast</p></div>
      <div class="item"><div class="item-row">The BIG BRO<span class="leader"></span><span class="price">€ 2,30</span></div><p class="desc">Croissant, Orangensaft und großer Cappuccino</p></div>
      <div class="item"><div class="item-row">The BIG BRO<span class="leader"></span><span class="price">€ 2,30</span></div><p class="desc">Müsli mit Joghurt und Obst</p></div>
    </div>

    <div class="divider" style="left:282px;top:300px;height:300px"></div>
    <div class="circle-mark" style="left:200px;top:285px;width:64px;height:64px"></div>

    <div class="block" style="left:60px;top:330px;width:205px">
      <p class="label">Coffe</p>
      <h3 class="display headline">Wake<br>Me Up</h3>
      <div class="drink"><span class="vol">0,3 l</span>Espresso<span class="leader"></span>€ 2,30</div>
      <div class="drink"><span class="vol">0,3 l</span>Cappuccino<span class="leader"></span>€ 2,30</div>
      <div class="drink"><span class="vol">0,3 l</span>Latte Macchiato<span class="leader"></span>€ 2,30</div>
      <div class="drink"><span class="vol">0,3 l</span>Milchkaffee<span class="leader"></span>€ 2,30</div>
      <div class="drink"><span class="vol">0,3 l</span>Flat White<span class="leader"></span>€ 2,30</div>
    </div>
  </div>
</section>

<!-- Spread 2: Burger -->
<section class="stage spread" style="top:1590px">
  <div class="page page-left">
    <div class="block" style="left:50px;top:70px;width:185px">
      <p class="label">Burger</p>
      <h3 class="display headline">Mouth<br>Meating</h3>
      <div class="item"><div class="item-row">The BIG BRO<span class="leader"></span><span class="price">€ 2,30</span></div><p class="desc">Rind, Cheddar, Salat und Tomate</p></div>
      <div class="item"><div class="item-row">The BIG BRO<span class="leader"></span><span class="price">€ 2,30</span></div><p class="desc">Rind, Bacon, Zwiebeln und Barbecuesauce</p></div>
      <div class="item"><div class="item-row">The BIG BRO<span class="leader"></span><span class="price">€ 2,30</span></div><p class="desc">Rind, Spiegelei, Gurke und Senf</p></div>
      <div class="item"><div class="item-row">The BIG BRO<span class="leader"></span><span class="price">€ 2,30</span></div><p class="desc">Doppelt Rind, Käse und Hausdressing</p></div>
    </div>
    <div class="divider" style="left:252px;top:130px;height:230px"></div>
    <div class="block" style="left:265px;top:60px;width:185px">
      <p class="label">Veggy Burger</p>
      <h3 class="display headline">Healthy<br>Tasty</h3>
      <div class="item"><div class="item-row">The BIG BRO<span class="leader"></span><span class="price">€ 2,30</span></div><p class="desc">Falafel, Hummus, Rucola und Tomate</p></div>
      <div class="item"><div class="item-row">The BIG BRO<span class="leader"></span><span class="price">€ 2,30</span></div><p class="desc">Halloumi, Paprika, Salat und Joghurtsauce</p></div>
      <div class="item"><div class="item-row">The BIG BRO<span class="leader"></span><span class="price">€ 2,30</span></div><p class="desc">Bohnenpatty, Avocado, Mais und Salsa</p></div>
      <div class="item"><div class="item-row">The BIG BRO<span class="leader"></span><span class="price">€ 2,30</span></div><p class="desc">Süßkartoffel, Spinat, Feta und Chili</p></div>
    </div>
    <div class="sand-panel" style="left:30px;top:460px;width:170px;height:190px"></div>
    <div class="photo" style="left:55px;top:440px;width:190px;height:170px;background:linear-gradient(135deg,#c98f60,#e3c39a 50%,#d2a243)" role="img" aria-label="Junge Frau in gelbem Pullover isst einen Burger"></div>
    <div class="rule" style="left:320px;top:480px;width:70px"></div>
    <p class="mood" style="left:320px;top:495px;width:70px">Mood<br>for<br>Food</p>
    <div class="rule" style="left:320px;top:560px;width:70px"></div>
  </div>
  <div class="page page-right">
    <div class="photo" style="inset:0;background:radial-gradient(ellipse at 40% 55%,#c98c4c 0,#8a5a2e 30%,#3a2c24 65%,#1f1b19 100%)" role="img" aria-label="Burger mit Sesambrötchen, Salat und Zwiebeln auf einem Holzbrett"></div>
    <h2 class="display vertical" style="right:14px;bottom:40px;font-size:50px;color:var(--sand)">Burger<span class="amp" style="color:#fff">and</span>Sauce</h2>
  </div>
</section>

<!-- Spread 3: Drinks -->
<section class="stage spread" style="top:2385px">
  <div class="page page-left">
    <div class="photo" style="inset:0;background:radial-gradient(ellipse at 55% 50%,#c8c47a 0,#6f7a3a 30%,#3d3526 65%,#231e1a 100%)" role="img" aria-label="Cocktail mit Limette und Minze auf Holztisch vor Lichterkette"></div>
    <h2 class="display vertical" style="left:20px;bottom:40px;font-size:50px;color:#fff">Cocktails<span class="amp">and</span>Wine</h2>
  </div>
  <div class="page page-right">
    <div class="block" style="left:40px;top:50px;width:165px">
      <p class="label">Cocktails</p>
      <h3 class="display headline">Shake it,<br>Baby</h3>
      <div class="drink"><span class="vol">0,3 l</span>Kolabrause<span class="leader"></span>€ 2,30</div>
      <div class="drink"><span class="vol">0,3 l</span>Kolabrause Zero<span class="leader"></span>€ 2,30</div>
      <div class="drink"><span class="vol">0,3 l</span>Fredo Mischmasch<span class="leader"></span>€ 2,30</div>
      <div class="drink"><span class="vol">0,3 l</span>Fredo Orange<span class="leader"></span>€ 2,30</div>
      <div class="drink"><span class="vol">0,3 l</span>Fredo Lemon<span class="leader"></span>€ 2,30</div>
      <div class="drink"><span class="vol">0,3 l</span>Talhofer Apfelschorle<span class="leader"></span>€ 2,30</div>
    </div>
    <div class="block" style="left:40px;top:230px;width:165px">
      <p class="label">Non Alkoholic</p>
      <h3 class="display headline">Fresh<br>and Cool</h3>
      <div class="drink"><span class="vol">0,3 l</span>Kolabrause<span class="leader"></span>€ 2,30</div>
      <div class="drink"><span class="vol">0,3 l</span>Kolabrause Zero<span class="leader"></span>€ 2,30</div>
      <div class="drink"><span class="vol">0,3 l</span>Fredo Mischmasch<span class="leader"></span>€ 2,30</div>
      <div class="drink"><span class="vol">0,3 l</span>Fredo Cola ohne Zucker<span class="leader"></span>€ 2,30</div>
    </div>
    <div class="block" style="left:40px;top:390px;width:165px">
      <p class="label">Alkoholic</p>
      <div class="drink"><span class="vol">0,3 l</span>Kolabrause<span class="leader"></span>€ 2,30</div>
      <div class="drink"><span class="vol">0,3 l</span>Kolabrause Zero<span class="leader"></span>€ 2,30</div>
      <div class="drink"><span class="vol">0,3 l</span>Fredo Mischmasch<span class="leader"></span>€ 2,30</div>
      <div class="drink"><span class="vol">0,3 l</span>Fredo Orange<span class="leader"></span>€ 2,30</div>
      <div class="drink"><span class="vol">0,3 l</span>Fredo Cola ohne Zucker<span class="leader"></span>€ 2,30</div>
      <div class="drink"><span class="vol">0,3 l</span>Fredo Lemon<span class="leader"></span>€ 2,30</div>
      <div class="drink"><span class="vol">0,3 l</span>Talhofer Rhabarberschorle<span class="leader"></span>€ 2,30</div>
    </div>
    <div class="divider" style="left:232px;top:120px;height:440px"></div>
    <div class="circle-mark" style="left:350px;top:40px;width:78px;height:78px;border-width:2px"></div>
    <div class="block" style="left:250px;top:130px;width:200px">
      <p class="label">Wine</p>
      <h3 class="display headline">Cheer<br>Me Up</h3>
      <div class="drink"><span class="vol">0,2 l</span>Riesling trocken<span class="leader"></span>€ 2,30</div>
      <div class="drink"><span class="vol">0,2 l</span>Grauburgunder<span class="leader"></span>€ 2,30</div>
      <div class="drink"><span class="vol">0,2 l</span>Weißburgunder<span class="leader"></span>€ 2,30</div>
      <div class="drink"><span class="vol">0,2 l</span>Rosé feinherb<span class="leader"></span>€ 2,30</div>
      <div class="drink"><span class="vol">0,2 l</span>Spätburgunder<span class="leader"></span>€ 2,30</div>
      <div class="drink"><span class="vol">0,2 l</span>Dornfelder<span class="leader"></span>€ 2,30</div>
      <div class="drink"><span class="vol">0,2 l</span>Merlot<span class="leader"></span>€ 2,30</div>
      <div class="drink"><span class="vol">0,2 l</span>Weinschorle weiß<span class="leader"></span>€ 2,30</div>
      <div class="drink"><span class="vol">0,2 l</span>Weinschorle rot<span class="leader"></span>€ 2,30</div>
      <div class="drink"><span class="vol">0,1 l</span>Secco<span class="leader"></span>€ 2,30</div>
      <div class="drink"><span class="vol">0,1 l</span>Sekt trocken<span class="leader"></span>€ 2,30</div>
    </div>
    <p class="mood" style="left:320px;top:440px;width:90px">Mood<br>for<br>Drinks</p>
    <div class="rule" style="left:320px;top:505px;width:90px"></div>
  </div>
</section>

</body>
</html>
```